HAIR EXTENSIONS

We need a web design for a company base in Chicago called Extensions by Corvina. We sale 100% human hair in Brazilian body wave deep wave straight or natural curl, Peruvian body wave straight or deep wave. Malaysian loose straight or body wave, in the chicago land.
We also ship hair to any city or country. We like to see design that use the colors pinks & grays, or would just like to see some design creative with colors thats inviting.

Also I'm using the tamsworth template, Home- banner contact us, about us, Features- product side/left sidebar, Shop- wish list /shopping cart/ tracking your order / checkout/ order received.
Porfolio-filterable 4column portfolio
Blog. Buy now

Industry/Entity Type

Hair

Number of Pages Required

4 page

Colors
aaaaaa
606060
dddddd
eea4c8
d3a5cc
b868aa
a6459a
ffc213
1b1b1b

Requirements
Must have
• I NEED THE DESIGNER TO DO THE 4 PAGE LIKE THIS.
• 1.HOME-PAGE BANNER CONTACT US SOME PRODUCT WITH SIDING IMAGES OF THE TOP PROUDCT
• 2.PRODUCT WITH SHOPPING CART- I WANT SIDING BARS FOR PRODUCT & SHOPPING CART WITH TRACKING YOUR ORDERS CHECK OUT & ORDER RECEIVED.
• 3.PORFOLIO PHOTO-I WANT A FEATURES FOR CUSTOMERS TO UPLOAN THERE PICTURE & BLOG ON THE PAGE
• 4.ABOUT US- TALK ABOUT ARE COMPAMY.
Nice to have
• hello designer
• I was working with a web developer for my site be for i came to pixelforgly & they build a site for me that i liked, You all can view it at www.Extensionsbycorvina.info
• long story short never could get them to finish the project after they got paid!!
• I know, why paid before its finish bad decision. So know I'm here starting over with you all.
• here is a list of my competition site
• www.tressvaultly.com
• www.lokawaves.com
• www.pellitashoppe.com
• So just to give some insight, I'm looking for something like the one i had builded.

```html
<!DOCTYPE html>
<html lang="en">
<head>
<meta charset="utf-8">
<title>Extensions by Corvina</title>
<link href="https://fonts.googleapis.com/css2?family=Roboto+Condensed:wght@300;400;700&family=Roboto:wght@400;500&display=swap" rel="stylesheet">
<style>
:root{
  --pink:#f37a82;
  --pink-light:#ff9a9a;
  --pink-soft:#fbc3c0;
  --maroon:#5b2127;
  --ink:#333333;
  --grey-text:#606060;
  --grey-band:#f1f1f1;
  --grey-line:#dddddd;
  --white:#ffffff;
}
*{box-sizing:border-box;margin:0;padding:0}
html,body{width:704px;height:1200px;overflow:hidden}
body{background:var(--white);font-family:"Roboto",Arial,sans-serif;color:var(--ink);position:relative}
.abs{position:absolute}

/* top bar */
.topbar{left:0;top:0;width:704px;height:41px;background:var(--grey-band);border-bottom:1px solid var(--pink)}
.topbar ul{position:absolute;left:47px;top:13px;display:flex;list-style:none}
.topbar li{height:27px;padding:0 9px;line-height:27px;font:400 7px/27px "Roboto Condensed",sans-serif;text-transform:uppercase;color:var(--white);background:var(--pink);border-right:1px solid #e46068;white-space:nowrap}
.topbar li.active{background:var(--maroon)}

/* header */
.header{left:0;top:41px;width:704px;height:64px;background:var(--grey-band)}
.logo{left:47px;top:20px;width:225px;font:400 19px/24px "Roboto Condensed",sans-serif;color:var(--pink);text-transform:uppercase;white-space:nowrap}
.search{left:282px;top:22px;width:141px;height:24px;display:flex}
.search .field{flex:1;background:var(--white);border:1px solid var(--grey-line)}
.search .btn{width:26px;background:var(--maroon);display:flex;align-items:center;justify-content:center}
.account{left:440px;top:20px;width:96px;text-align:right;font:400 6.5px/10px "Roboto Condensed",sans-serif;text-transform:uppercase;color:var(--ink);white-space:nowrap}
.cart{left:547px;top:15px;width:110px;height:34px;background:var(--white);border:1px solid var(--grey-line);padding:5px 8px}
.cart b{display:block;font:400 11px/13px "Roboto Condensed",sans-serif;color:var(--pink);text-transform:uppercase}
.cart span{display:block;font:400 6px/9px "Roboto Condensed",sans-serif;color:var(--grey-text);white-space:nowrap}
.cart svg{position:absolute;right:8px;top:14px}

/* navigation */
.nav{left:0;top:105px;width:704px;height:36px;background:var(--white);border-top:1px solid var(--grey-line);border-bottom:3px solid var(--grey-band)}
.nav ul{position:absolute;left:47px;top:0;display:flex;list-style:none;height:32px}
.nav li{padding:6px 9px 0;font:400 7.5px/9px "Roboto Condensed",sans-serif;color:var(--grey-text);border-left:1px solid var(--grey-line);white-space:nowrap}
.nav li:last-child{border-right:1px solid var(--grey-line)}

/* banner */
.banner{left:47px;top:156px;width:610px;height:192px;display:flex}
.banner .photo{width:365px;background:linear-gradient(120deg,#f7d9a8 0%,#d99060 40%,#9a4e30 75%,#f0c29a 100%)}
.banner .promo{flex:1;background:linear-gradient(135deg,#fbb2ac,#f47c80);text-align:center;color:var(--white);padding-top:58px}
.promo .kicker{font:400 12px/14px "Roboto Condensed",sans-serif;text-transform:uppercase}
.promo .headline{font:400 22px/26px "Roboto Condensed",sans-serif;text-transform:uppercase;color:var(--maroon);margin:4px 0 12px}
.btn-dark{display:inline-block;background:var(--maroon);color:var(--white);font:400 9px/1 "Roboto Condensed",sans-serif;text-transform:uppercase;padding:9px 18px}

/* category tiles */
.tile{top:361px;width:193px;height:104px;background:var(--grey-band);overflow:hidden}
.tile .pic{position:absolute;right:0;top:0;width:95px;height:104px}
.tile .copy{position:absolute;left:10px;top:10px;font:300 18px/17px "Roboto Condensed",sans-serif;text-transform:uppercase;color:var(--ink)}
.tile .copy .lead{color:var(--pink)}
.tile .copy .big{font-size:24px;line-height:22px;font-weight:400}
.tile .copy .sub{font-size:16px;color:var(--grey-text)}
.btn-pink{display:inline-block;background:var(--pink);color:var(--white);font:400 7px/1 "Roboto Condensed",sans-serif;text-transform:uppercase;padding:7px 10px;margin-top:4px}

/* featured */
.section-title{left:47px;top:476px;width:610px;padding-bottom:6px;border-bottom:1px solid var(--pink);font:400 10px/12px "Roboto Condensed",sans-serif;text-transform:uppercase}
.product{width:141px;height:241px;border:1px solid var(--grey-line);background:var(--white);text-align:center}
.product .pic{position:absolute;left:25px;top:12px;width:90px;height:110px;border-radius:4px}
.product .name{position:absolute;left:0;top:135px;width:139px;height:28px;background:var(--grey-band);display:flex;align-items:center;justify-content:center;padding:0 12px;font:400 6.5px/8px "Roboto Condensed",sans-serif;text-transform:uppercase;color:var(--pink)}
.product .desc{position:absolute;left:8px;top:168px;width:123px;font:400 6.5px/10px "Roboto",sans-serif;color:var(--ink)}
.product .price{position:absolute;left:0;top:192px;width:139px;font:400 11px/13px "Roboto Condensed",sans-serif}
.product .add{position:absolute;left:40px;top:208px;width:60px;height:22px;background:linear-gradient(var(--pink-light),var(--pink));color:var(--white);font:400 6.5px/22px "Roboto Condensed",sans-serif;text-transform:uppercase}

/* footer */
.footer{left:0;top:1026px;width:704px;height:127px;background:var(--grey-band)}
.footer .col{position:absolute;top:32px;font:400 6.5px/14px "Roboto Condensed",sans-serif;text-transform:uppercase;color:var(--ink)}
.footer .col h4{font:400 8px/10px "Roboto Condensed",sans-serif;color:var(--maroon);margin-bottom:5px}
.bottombar{left:0;top:1153px;width:704px;height:47px;background:var(--white);border-top:1px solid var(--grey-line)}
.bottombar .credit{position:absolute;left:47px;top:15px;font:400 6px/8px "Roboto",sans-serif;color:var(--ink)}
.social{position:absolute;top:11px;width:15px;height:15px;border-radius:50%;background:var(--pink)}
</style>
</head>
<body>

<div class="abs topbar">
  <ul>
    <li class="active">Home</li><li>Wish List (0)</li><li>My Account</li><li>Shopping Cart</li><li>Checkout</li>
  </ul>
</div>

<header class="abs header">
  <div class="abs logo">Extensions by Corvina</div>
  <div class="abs search">
    <div class="field"></div>
    <div class="btn"><svg width="9" height="9" viewBox="0 0 10 10"><circle cx="4" cy="4" r="3" fill="none" stroke="#fff" stroke-width="1.4"/><line x1="6.2" y1="6.2" x2="9" y2="9" stroke="#fff" stroke-width="1.4"/></svg></div>
  </div>
  <div class="abs account">Login<br>Create an account</div>
  <div class="abs cart">
    <b>Cart:</b><span>0 item(s) - $0.00</span>
    <svg width="7" height="5" viewBox="0 0 7 5"><path d="M0 0 L3.5 4 L7 0" fill="none" stroke="#606060"/></svg>
  </div>
</header>

<nav class="abs nav">
  <ul>
    <li>Installation<br>Supplies ⌄</li>
    <li>U-tip Individual<br>Extensions</li>
    <li>I-tip Individual<br>Extensions</li>
    <li>Weft<br>Hair</li>
    <li>Clip-in<br>Hair</li>
    <li>Keratin &amp; Glue<br>Supplies</li>
    <li>Microlinks, Locks &amp;<br>Supplies</li>
  </ul>
</nav>

<section class="abs banner">
  <div class="photo" role="img" aria-label="Portrait of a woman with long auburn hair in warm sunlight"></div>
  <div class="promo">
    <div class="kicker">Get everything you need for</div>
    <div class="headline">Hair Extension!</div>
    <span class="btn-dark">Shop now!</span>
  </div>
</section>

<div class="abs tile" style="left:47px">
  <div class="pic" role="img" aria-label="Long straight brown wefted hair" style="background:linear-gradient(90deg,#f1f1f1,#8a5a3e 40%,#5a3424)"></div>
  <div class="copy"><span class="lead">Wefted</span><br><span class="big">Hair</span><br><span class="sub">Extensions</span><br><span class="btn-pink">Shop now!</span></div>
</div>
<div class="abs tile" style="left:256px">
  <div class="pic" role="img" aria-label="Blonde clip-in hair extensions" style="background:linear-gradient(90deg,#f1f1f1,#e8c9a0 45%,#c99a66)"></div>
  <div class="copy"><span class="lead">Clip in</span><br><span class="big">Hair</span><br><span class="sub">Extensions</span><br><span class="btn-pink">Shop now!</span></div>
</div>
<div class="abs tile" style="left:465px">
  <div class="pic" role="img" aria-label="Woman with long flowing brown hair" style="background:linear-gradient(90deg,#f1f1f1,#c58a64 45%,#8c5434)"></div>
  <div class="copy"><span class="lead">Keratin</span><br><span class="big">&amp; Glue</span><br><span class="sub">Supplies</span><br><span class="btn-pink" style="background:var(--maroon)">Shop now!</span></div>
</div>

<h2 class="abs section-title">Featured Products</h2>

<div class="abs product" style="left:47px;top:512px"><div class="pic" role="img" aria-label="Hair bow clip with comb" style="background:radial-gradient(#d9a478,#f7efe8 70%)"></div><div class="name">Excepteur sint occaecat cupidatat non</div><div class="desc">How do you think, what makes women the most beautiful and unpred...</div><div class="price">$258.96</div><div class="add">Add to cart</div></div>
<div class="abs product" style="left:204px;top:512px"><div class="pic" role="img" aria-label="Ash blonde straight weft" style="background:radial-gradient(#c9b296,#f8f4ef 70%)"></div><div class="name">Lorem ipsum dolor sit amet conse ctetur</div><div class="desc">How do you think, what makes women the most beautiful and unpred...</div><div class="price">$258.96</div><div class="add">Add to cart</div></div>
<div class="abs product" style="left:360px;top:512px"><div class="pic" role="img" aria-label="Straight brown clip-in set" style="background:radial-gradient(#8a4e2c,#f6efe9 70%)"></div><div class="name">Adipisicing elit, sed do eiusmod tempor incididunt ut</div><div class="desc">How do you think, what makes women the most beautiful and unpred...</div><div class="price">$258.96</div><div class="add">Add to cart</div></div>
<div class="abs product" style="left:516px;top:512px"><div class="pic" role="img" aria-label="Wavy brown hair weft" style="background:radial-gradient(#94603a,#f6efe9 70%)"></div><div class="name">Sed do eiusmod tempor incididunt ut</div><div class="desc">How do you think, what makes women the most beautiful and unpred...</div><div class="price">$258.96</div><div class="add">Add to cart</div></div>

<div class="abs product" style="left:47px;top:768px"><div class="pic" role="img" aria-label="Purple clip-in hair strands" style="background:radial-gradient(#8a2a9a,#f5eef6 70%)"></div><div class="name">Eiusmod tempor incididunt ut</div><div class="desc">How do you think, what makes women the most beautiful and unpred...</div><div class="price">$258.96</div><div class="add">Add to cart</div></div>
<div class="abs product" style="left:204px;top:768px"><div class="pic" role="img" aria-label="Dark brown keratin-tip extensions" style="background:radial-gradient(#4a2a1c,#f3eeeb 70%)"></div><div class="name">Esse cillum dolore eu fugiat nulla pariatur</div><div class="desc">How do you think, what makes women the most beautiful and unpred...</div><div class="price">$258.96</div><div class="add">Add to cart</div></div>
<div class="abs product" style="left:360px;top:768px"><div class="pic" role="img" aria-label="Braided blonde bun hairpiece" style="background:radial-gradient(#bfa27c,#f7f2ec 70%)"></div><div class="name">Dolore eu fugiat nulla pariatur</div><div class="desc">How do you think, what makes women the most beautiful and unpred...</div><div class="price">$258.96</div><div class="add">Add to cart</div></div>
<div class="abs product" style="left:516px;top:768px"><div class="pic" role="img" aria-label="Straight brown tape-in extension" style="background:radial-gradient(#6a3a26,#f4eeea 70%)"></div><div class="name">Excepteur sint occaecat cupidatat non</div><div class="desc">How do you think, what makes women the most beautiful and unpred...</div><div class="price">$258.96</div><div class="add">Add to cart</div></div>

<footer class="abs footer">
  <div class="col" style="left:47px"><h4>Information</h4>About<br>Delivery<br>Privacy Policy<br>Terms &amp; Conditions</div>
  <div class="col" style="left:203px"><h4>Customer Service</h4>Contact Us<br>Returns<br>Site Map</div>
  <div class="col" style="left:360px"><h4>Extras</h4>Brands<br>Affiliates<br>Specials</div>
  <div class="col" style="left:516px"><h4>My Account</h4>My Account<br>Order History<br>Wish List<br>Newsletter</div>
</footer>

<div class="abs bottombar">
  <div class="credit">Powered by Loomvale Studio Extensions by Corvina © 2014</div>
  <span class="social" style="left:594px"></span>
  <span class="social" style="left:616px"></span>
  <span class="social" style="left:638px"></span>
</div>

</body>
</html>
```